Fitness Centre/Personal Trainer Business Card

We need a business card design for a company based in Singapore called 'Vigor Lattice'.

We are a team of Personal Trainers and we are planning to open our new training facility.

This design will also be printed/painted on the walls in our gym.

We are a new breed of personal trainers who take fitness seriously and holistically. We do not merely train our clients to be big and muscular.

We believe in wholeness. In our opinion, fitness should include: strength, speed, flexibility, mobility, stamina & agility. These are what we train for. Of course, nutrition/diet is key.

We use fitness tools such as kettlebells, QLM, Pylometric boxes, battling ropes, clubbells, medicine balls, bulgarian bags etc - functional and non-bulky tools.

I currently have a Facebook page 'Vigor Lattice SG' which shows a logo of a kettlebell. But my business focus has since changed.

Services provided:
- Kettlebell Sport Preparation
- Calisthenics Training
- Corrective Exercises
- Sports Strength & Conditioning
- 28 days Weight Loss Program
- Myofascial Rehab Therapy
- Sports/Thai Massage

Main colors for the design should be BLACK & YELLOW. We envision a design which is able to protray the holistic view we take on fitness. Also it should somewhat appeal to the ladies and not intimidate them.

Target Market(s)

People between 18-35 years old. Students and working class alike.

Industry/Entity Type

Training

Requirements
Must have
• Name: Marcus Oriel Boon
Fitness Coach
Corrective Exercise Specialist
M: +65 9042 7736
E: marcus@sgvigorlattice.example

Double-sided please.
Nice to have
• "Where does your vigor lattice stand?"

```html
<!DOCTYPE html>
<html lang="en">
<head>
<meta charset="utf-8">
<title>Vigor Lattice – Business Card</title>
<link rel="stylesheet" href="https://fonts.googleapis.com/css2?family=Open+Sans:wght@700;800&family=PT+Sans+Narrow:wght@700&family=Arimo:wght@400&display=swap">
<style>
  :root {
    --ink: #353535;
    --yellow: #fdef14;
    --yellow-deep: #f3e51a;
    --olive: #7a7326;
    --paper: #fdf9f9;
    --page: #ffffff;
    --label: #3a3a3a;
  }
  html, body {
    margin: 0;
    padding: 0;
    width: 1200px;
    height: 1134px;
    overflow: hidden;
    background: var(--page);
  }
  .sheet { display: block; width: 1200px; height: 1134px; }
  .card-frame { fill: var(--paper); stroke: var(--ink); stroke-width: 4; }
  .card-back { fill: var(--ink); }
  .band-yellow { fill: var(--yellow); }
  .panel-dark { fill: var(--ink); }
  .name-line { fill: none; stroke: var(--ink); stroke-width: 3; }
  .title-rule { stroke: var(--ink); stroke-width: 8; }
  .person-name {
    font-family: "Open Sans", sans-serif;
    font-weight: 800;
    font-size: 33px;
    fill: var(--ink);
  }
  .role-coach {
    font-family: "Open Sans", sans-serif;
    font-weight: 700;
    font-size: 22px;
    fill: var(--ink);
  }
  .role-specialist {
    font-family: "PT Sans Narrow", sans-serif;
    font-weight: 700;
    font-size: 34px;
    fill: var(--ink);
  }
  .contact {
    font-family: "PT Sans Narrow", sans-serif;
    font-weight: 700;
    font-size: 28px;
    fill: var(--ink);
  }
  .tagline {
    font-family: "PT Sans Narrow", sans-serif;
    font-weight: 700;
    font-size: 31px;
    fill: var(--yellow);
  }
  .tagline-rule { fill: var(--yellow); }
  .side-label {
    font-family: "Arimo", sans-serif;
    font-weight: 400;
    font-size: 96px;
    fill: var(--label);
    letter-spacing: 4px;
  }
</style>
</head>
<body>
<svg class="sheet" viewBox="0 0 1250 1181" xmlns="http://www.w3.org/2000/svg">
  <defs>
    <linearGradient id="stripe-fade" gradientUnits="userSpaceOnUse" x1="643" y1="0" x2="960" y2="0">
      <stop offset="0" stop-color="var(--olive)"/>
      <stop offset="1" stop-color="var(--yellow)"/>
    </linearGradient>
    <linearGradient id="training-fill" x1="0" y1="0" x2="1" y2="1">
      <stop offset="0" stop-color="#9a9a9a"/>
      <stop offset="0.6" stop-color="#c9c9c9"/>
      <stop offset="1" stop-color="#efe49a"/>
    </linearGradient>
  </defs>

  <!-- Front side -->
  <g class="card-front">
    <rect class="card-frame" x="3" y="3" width="604" height="1077"/>

    <polygon class="training-art" role="img"
      aria-label="Silhouettes of people training – push-ups, squats and running – along a yellow measuring tape"
      fill="url(#training-fill)"
      points="25,20 535,20 535,190 60,470 25,470"/>

    <polygon class="panel-dark" points="205,578 607,270 607,940"/>
    <polygon class="band-yellow" points="3,545 607,95 607,270 3,725"/>

    <polygon class="band-yellow" points="312,520 607,298 607,315 378,483 445,497 607,375 607,395 395,545"/>
    <polygon class="band-yellow" points="410,555 607,405 607,425 485,517 545,532 607,485 607,505 490,582"/>
    <polygon class="band-yellow" points="512,598 607,525 607,620"/>

    <path class="name-line" d="M85,568 L310,402 Q330,392 335,410 Q342,428 365,412 L525,295"/>
    <text class="person-name" transform="translate(86,550) rotate(-38)">Marcus Oriel Boon</text>
    <text class="role-coach" transform="translate(352,405) rotate(-38)">Fitness Coach</text>

    <line class="title-rule" x1="185" y1="658" x2="558" y2="1000"/>
    <text class="role-specialist" transform="translate(226,662) rotate(41)">Corrective Exercise Specialist</text>

    <text class="contact" x="27" y="1007">+65 9042 7736</text>
    <text class="contact" x="27" y="1045">marcus@sgvigorlattice.example</text>
  </g>

  <!-- Back side -->
  <g class="card-reverse">
    <rect class="card-back" x="643" y="3" width="595" height="1077"/>
    <polygon fill="url(#stripe-fade)" points="643,215 1145,35 1230,82 643,298"/>
    <polygon fill="url(#stripe-fade)" points="643,355 1075,205 1158,252 643,438"/>
    <polygon fill="url(#stripe-fade)" points="643,510 1008,380 1093,428 643,590"/>
    <polygon fill="url(#stripe-fade)" points="643,665 952,555 1037,603 643,745"/>

    <text class="tagline" x="944" y="968" text-anchor="middle" textLength="470" lengthAdjust="spacingAndGlyphs">“Where does your vigor lattice stand?”</text>
    <polygon class="tagline-rule" points="708,980 1180,978 1180,990 708,990"/>
  </g>

  <text class="side-label" x="303" y="1172" text-anchor="middle">FRONT</text>
  <text class="side-label" x="940" y="1172" text-anchor="middle">BACK</text>
</svg>
</body>
</html>
```